Kickass billboard for motorway

We take dented trucks - clue is in the name.
We have a 45ft billboard we're looking to design constructed from an old trailer we own (so we can be as creative as possible).
We provide a van buying service, being one of the only companies in the UK with the facilities to recover faulty, damaged and broken vans - from small car derived vans to large trucks and lorries.
ur niche in the market is different to car buying services, as buying and selling cars is often an emotionally driven process, whereas people often see and treat vans purely as a tool. There are alternatives to a car, public transport etc, but not to a work van - so people go out straight away and replace them immediately, often leaving the old broken van to sit on their drive or in their unit.
Looking to start building a brand asset bank.
Feel free to check out our website to get a feel for what we do:
Wetakedentedtrucks.co.uk

Target Market(s)

Van owners/drivers & fleet managers

Industry/Entity Type

Automotive

Font styles to use
Sans Serif

Colors
34a7d8

Requirements
Must have
• Eye-catching - very eye-catching.
We want to advertise the fact we collect vehicles for free.
We pay instantly upon arrival.
Our phone number 0161 473 2046
Our website www.wetakedentedtrucks.co.uk
Nice to have
• 3d elements - we have the ability to get 3d props for the billboard including damaged vans etc.

```html
<!DOCTYPE html>
<html lang="en">
<head>
<meta charset="utf-8">
<title>We take dented trucks – motorway billboard</title>
<link rel="stylesheet" href="https://fonts.googleapis.com/css2?family=Fredoka:wght@400;500;600&display=swap">
<style>
  :root {
    --navy: #1d3a73;
    --navy-deep: #1a3266;
    --sky: #55ace0;
    --brand-blue: #34a7d8;
    --yellow: #fcea05;
    --white: #ffffff;
    --page: #ffffff;
    --van-orange: #f0a12c;
    --van-cream: #e9e6df;
  }
  * { margin: 0; padding: 0; box-sizing: border-box; }
  html, body {
    width: 1200px; height: 1000px; overflow: hidden;
    background: var(--page);
    font-family: "Fredoka", "Arial Rounded MT Bold", sans-serif;
  }
  .billboard {
    position: absolute; left: 40px; top: 330px;
    width: 1120px; height: 340px;
    overflow: hidden;
    box-shadow: 0 18px 30px -14px rgba(0,0,0,0.35);
  }
  .billboard__art { position: absolute; inset: 0; }
  .brand {
    position: absolute; left: 40px; top: 30px;
    display: flex; align-items: center; gap: 14px;
  }
  .brand__mark {
    width: 26px; height: 26px; background: var(--brand-blue);
  }
  .brand__name {
    font-weight: 600; font-size: 40px; line-height: 1;
    color: var(--white); letter-spacing: -0.5px;
  }
  .offer {
    position: absolute; left: 36px; top: 110px; width: 520px;
  }
  .offer__headline {
    font-weight: 600; font-size: 42px; line-height: 44px;
    color: var(--navy-deep);
  }
  .offer__sub {
    margin-top: 6px;
    font-weight: 500; font-size: 22px; line-height: 1;
    color: var(--brand-blue);
  }
  .contact {
    position: absolute; left: 36px; top: 262px;
  }
  .contact__phone {
    display: flex; align-items: center; gap: 8px;
    font-weight: 600; font-size: 33px; line-height: 1;
    color: var(--yellow);
  }
  .contact__phone svg { width: 28px; height: 28px; }
  .contact__web {
    margin: 6px 0 0 92px;
    font-weight: 500; font-size: 18px; line-height: 1;
    color: var(--white);
  }
  .van-photo {
    position: absolute; left: 750px; top: 28px;
    width: 250px; height: 284px;
    border-radius: 18px;
    background: linear-gradient(180deg, var(--van-cream) 0%, var(--van-cream) 18%, var(--van-orange) 45%, var(--van-orange) 78%, #3a3430 100%);
  }
</style>
</head>
<body>
<section class="billboard">
  <svg class="billboard__art" viewBox="0 0 1120 340" aria-hidden="true">
    <defs>
      <linearGradient id="bg" x1="0" y1="0" x2="1" y2="0">
        <stop offset="0" stop-color="var(--navy)"/>
        <stop offset="0.45" stop-color="var(--navy)"/>
        <stop offset="1" stop-color="var(--sky)"/>
      </linearGradient>
    </defs>
    <rect class="backdrop" width="1120" height="340" fill="url(#bg)"/>
    <g class="rings" fill="none" stroke="var(--white)" stroke-width="2" opacity="0.85">
      <circle cx="875" cy="168" r="150"/>
      <circle cx="875" cy="168" r="210"/>
      <circle cx="875" cy="168" r="270"/>
      <circle cx="875" cy="168" r="330"/>
    </g>
    <rect class="offer-band" x="0" y="104" width="552" height="146" fill="var(--yellow)"/>
    <polygon class="offer-arrow" points="548,48 682,176 548,306" fill="var(--yellow)"/>
  </svg>

  <div class="brand">
    <span class="brand__mark"></span>
    <span class="brand__name">wetakedentedtrucks</span>
  </div>

  <div class="offer">
    <h1 class="offer__headline">Get instant CASH<br>from your broken van</h1>
    <p class="offer__sub">AND WE COLLECT VEHICLES FOR FREE!</p>
  </div>

  <div class="contact">
    <p class="contact__phone">
      <svg viewBox="0 0 24 24" aria-hidden="true"><path fill="var(--yellow)" d="M6.6 10.8a15.1 15.1 0 0 0 6.6 6.6l2.2-2.2a1 1 0 0 1 1-.25 11.4 11.4 0 0 0 3.6.57 1 1 0 0 1 1 1V20a1 1 0 0 1-1 1A17 17 0 0 1 3 4a1 1 0 0 1 1-1h3.5a1 1 0 0 1 1 1c0 1.25.2 2.45.57 3.57a1 1 0 0 1-.25 1z"/></svg>
      CALL NOW! 0161 473 2046
    </p>
    <p class="contact__web">www.wetakedentedtrucks.co.uk</p>
  </div>

  <div class="van-photo" role="img" aria-label="Photo of an orange and cream classic van bursting through torn paper"></div>
</section>
</body>
</html>
```